LIFE CHANGING NEW WEBSITE DESIGN NEEDED FOR FULL WEBSITE- FUN/FEMININE!

I need a website designed for a personal financial advice website geared at women called DAME CLOVER HAVEN. I will be providing free financial advice around topics of making, saving, spending and sharing money. The concept is to change the way women understand money and the necessity around building various passive income streams to ensure full financial freedom. This will then carry down to advice for mothers with children and children in particular. The website should be elegant and yet witty. I don't want lots of serious photos but more relatable. I will have a photo of myself and my story as this is a blog and needs to be relatable to women and mothers. I like pinks and greys. I want to have a pink piggy bank being broken with a hammer in the front screen to break our traditional mindset around piggy bank saving/spending habits. I have created a logo that is a pink piggy head with DAME CLOVER HAVEN that needs to be incorporated so that it blends into the heading. I have also already started designing the website on Squarespace and can provide access to that. Basically it should have a format of DAME CLOVER HAVEN LOGO center in header then on left hand navigation: MAKE, SAVE, SPEND, SHARE then on right hand header navigation: MISSION, GET STARTED, CONTACT DCH I would like to have the front page when you go to the url to have the image of the piggy bank being broken then a catchy phrase then under 4 boxes with MAKE (image and description) SAVE (image and description) SPEND (image and description) SHARE (image and description) if you click on those or the title they go to pages that are dedicated to each them. Each page should have a little intro on the topic then I want lots of blog links as I will be mainly writing blogs. Each blog site should have ability to write comments as well. I need social media icons on each page too. Please let me know what you need from me to get started. I prefer having a discussion if possible to not waste anyone's time. I need the site to be easy for me to use and add blogs/urls etc as needed. I also need the site to be put into my domain that I already purchased: www.damecloverhaven.com

Target Market(s)

teenage girls, 20 something girls, 30 something girls and mothers

Coding

Coded - Design and coding required

Number of Pages Required

5+ page

Font styles to use
Sans Serif

Colors
e667a6
e34197
f59195
eea4c8
aaaaaa
cbcbcb
959595

Requirements
Must have
• TOP NAVIGATION
• MAKE SAVE SPEND SHARE LOGO/DAME CLOVER HAVEN MISSION GET STARTED CONTACT DCH
• FRONT PAGE: IMAGE OF PIGGY BANK BEING BROKEN WITH A HAMMER
• CATCH PHRASE OVER THE IMAGE
• BUTTON IN PINK- TAKE ACTION (WHICH DIRECTS TO TAKE ACTION TAB ON NAVIGATION HEADER
• 4 BOXES BELOW MAIN IMAGE WITH IMAGE/DESCRIPTIONS FOR MAKE, SAVE, SPEND, SHARE THAT EACH GO TO THE PAGES FROM THE NAVIGATION HEADER
• EACH PAGE SHOULD BE DEDICATED TO THOSE TOPICS THEN THERE IS AN INTRO ON EACH PAGE THEN THE LINKS TO DIFFERENT BLOGS AROUND EACH TOPIC FOR MAKE, SAVE, SPEND, SHARE
• EACH BLOG SHOULD HAVE COMMENTS SECTION AND SOCIAL MEDIA ICONS
• (GOOD TO USE PINKS/GREYS)
Should not have
• BE SUPER BUSY, CLUTTERED, FEEL LIKE I AM SELLING SOMETHING

```html
<!DOCTYPE html>
<html lang="en">
<head>
<meta charset="utf-8">
<title>Dame Clover Haven</title>
<link href="https://fonts.googleapis.com/css2?family=Montserrat:wght@500;600;700&family=Lato:wght@400;700&display=swap" rel="stylesheet">
<style>
:root{
  --pink:#e34197;
  --pink-soft:#e667a6;
  --coral:#f28c90;
  --blush:#fdeef6;
  --ink:#2e2e2e;
  --grey:#959595;
  --grey-mid:#aaaaaa;
  --grey-light:#f5f5f5;
  --white:#ffffff;
}
*{margin:0;padding:0;box-sizing:border-box}
html,body{width:688px;height:1200px;overflow:hidden;background:var(--white)}
body{position:relative;font-family:'Lato',sans-serif;color:var(--ink)}
.abs{position:absolute}
.site-header{left:0;top:0;width:688px;height:59px;background:var(--blush)}
.nav-link{position:absolute;top:28px;font-size:6.4px;letter-spacing:.3px;color:var(--ink)}
.nav-link.active{color:var(--pink)}
.brand{position:absolute;left:0;width:688px;text-align:center;top:29px;font-family:'Montserrat',sans-serif;font-weight:500;font-size:9.5px;color:var(--pink)}
.brand-dot{position:absolute;left:338px;top:14px;width:12px;height:12px;border:1.2px solid var(--pink-soft);border-radius:50%}
.hero{left:0;top:59px;width:688px;height:229px;background:linear-gradient(90deg,#e9b7cc 0%,#ece6e6 22%,#f2f2f2 55%,#e6e6e6 100%)}
.hero-title{position:absolute;left:0;width:688px;top:68px;text-align:center;font-family:'Montserrat',sans-serif;font-weight:700;font-size:22.5px;line-height:26px;color:var(--ink)}
.btn-round{position:absolute;left:303px;top:133px;width:82px;height:23px;border-radius:12px;background:var(--pink);color:var(--white);font-family:'Montserrat',sans-serif;font-weight:600;font-size:6.4px;letter-spacing:.4px;line-height:23px;text-align:center}
.hero-arrow{position:absolute;top:101px;width:32px;height:32px;background:rgba(90,90,90,.75)}
.hero-dot{position:absolute;top:202px;width:7px;height:7px;border-radius:50%;background:var(--ink)}
.hero-dot.on{background:var(--pink)}
.topic-card{position:absolute;top:316px;width:97px;text-align:center}
.topic-photo{width:97px;height:65px;border:.5px solid #ddd}
.topic-title{margin-top:8px;font-family:'Montserrat',sans-serif;font-weight:500;font-size:9px}
.topic-text{margin-top:4px;font-size:5.9px;line-height:8.6px;letter-spacing:.1px}
.welcome-band{left:0;top:458px}
.welcome-title{left:135px;top:516px;font-family:'Montserrat',sans-serif;font-weight:500;font-size:8.8px}
.welcome-text{left:135px;width:202px;font-size:5.9px;line-height:8.6px;text-align:justify}
.btn-square{position:absolute;background:var(--pink);color:var(--white);font-family:'Montserrat',sans-serif;font-weight:600;font-size:6px;text-align:center}
.section-title{left:0;width:688px;top:722px;text-align:center;font-family:'Montserrat',sans-serif;font-weight:500;font-size:9px;letter-spacing:.3px}
.news-card{position:absolute;top:748px;width:131px}
.news-photo{position:relative;width:131px;height:87px}
.news-date{position:absolute;left:6px;top:79px;width:58px;height:18px;background:var(--grey-mid);color:var(--white);font-family:'Montserrat',sans-serif;font-weight:600;font-size:6.5px;line-height:18px;text-align:center}
.news-title{margin-top:17px;font-family:'Montserrat',sans-serif;font-weight:600;font-size:6px;line-height:8.6px}
.news-text{margin-top:5px;font-size:5.9px;line-height:8.6px;color:#666}
.newsletter{left:0;top:973px;width:688px;height:98px;background:var(--coral);text-align:center;color:var(--white)}
.newsletter h2{margin-top:23px;font-family:'Montserrat',sans-serif;font-weight:700;font-size:10.2px;letter-spacing:.2px}
.newsletter p{margin-top:3px;font-size:4.8px}
.email-field{position:absolute;left:260px;top:57px;width:168px;height:16px;background:var(--white);border-radius:2px;text-align:left;padding-left:9px;font-size:3.8px;line-height:16px;color:var(--grey-mid)}
.site-footer{left:0;top:1071px;width:688px;height:129px;background:var(--blush)}
.footer-brand{position:absolute;left:135px;width:97px;top:50px;text-align:center;font-family:'Montserrat',sans-serif;font-weight:500;font-size:8.2px;color:var(--pink)}
.footer-divider{position:absolute;left:231px;top:18px;width:.6px;height:54px;background:#d9c3cf}
.contact-icon{position:absolute;top:31px;width:18px;height:18px;border-radius:50%;background:var(--white)}
.contact-icon svg{position:absolute;left:5px;top:5px}
.contact-text{position:absolute;top:32px;font-size:5.7px;line-height:9.3px}
.footer-rule{position:absolute;left:0;top:92px;width:688px;height:.6px;background:#e8d3de}
.copyright{position:absolute;left:135px;top:108px;font-size:4.8px}
.social{position:absolute;top:112px;width:14px;height:14px;border-radius:50%;background:var(--pink)}
</style>
</head>
<body>

<header class="abs site-header">
  <span class="nav-link active" style="left:135px">MAKE</span>
  <span class="nav-link" style="left:170px">SAVE</span>
  <span class="nav-link" style="left:206px">SPEND</span>
  <span class="nav-link" style="left:246px">SHARE</span>
  <span class="brand-dot"></span>
  <div class="brand">Dame Clover Haven</div>
  <span class="nav-link" style="left:408px">MONEY</span>
  <span class="nav-link" style="left:445px">EXPERT</span>
  <span class="nav-link" style="left:483px">MISSION</span>
  <span class="nav-link" style="left:524px">CONTACT</span>
</header>

<section class="abs hero" role="img" aria-label="A man raising a hammer over a pink piggy bank on a desk">
  <span class="hero-arrow" style="left:40px">
    <svg width="32" height="32" viewBox="0 0 32 32"><path d="M18 10 L12 16 L18 22" fill="none" stroke="#fff" stroke-width="1.6"/></svg>
  </span>
  <h1 class="hero-title">CONTROL YOUR PIGGY<br>OBTAIN FINANCIAL FREEDOM</h1>
  <span class="btn-round">TAKE ACTION</span>
  <span class="hero-arrow" style="left:617px">
    <svg width="32" height="32" viewBox="0 0 32 32"><path d="M14 10 L20 16 L14 22" fill="none" stroke="#fff" stroke-width="1.6"/></svg>
  </span>
  <span class="hero-dot on" style="left:329px"></span>
  <span class="hero-dot" style="left:340px"></span>
  <span class="hero-dot" style="left:351px"></span>
</section>

<article class="topic-card" style="left:135px">
  <div class="topic-photo" role="img" aria-label="Woman kissing a pink piggy bank" style="background:linear-gradient(90deg,#c9a79a,#f3dde3)"></div>
  <h3 class="topic-title">MAKE</h3>
  <p class="topic-text">Lorem ipsum dolor sit amet, con-sectetur adipiscing elit. Fusce a laoreet massa, in euismod ligula. Curabitur a vulputate purus.</p>
</article>
<article class="topic-card" style="left:242px">
  <div class="topic-photo" role="img" aria-label="Smiling woman holding a piggy bank and banknotes" style="background:linear-gradient(90deg,#f4c9d6,#eee0da)"></div>
  <h3 class="topic-title">SAVE</h3>
  <p class="topic-text">Lorem ipsum dolor sit amet, con-sectetur adipiscing elit. Fusce a laoreet massa, in euismod ligula. Curabitur a vulputate purus.</p>
</article>
<article class="topic-card" style="left:350px">
  <div class="topic-photo" role="img" aria-label="Hands passing a small gold piggy bank" style="background:linear-gradient(90deg,#dcd2c4,#ececec)"></div>
  <h3 class="topic-title">SPEND</h3>
  <p class="topic-text">Lorem ipsum dolor sit amet, con-sectetur adipiscing elit. Fusce a laoreet massa, in euismod ligula. Curabitur a vulputate purus.</p>
</article>
<article class="topic-card" style="left:457px">
  <div class="topic-photo" role="img" aria-label="Coin stacks beside a pink piggy bank" style="background:linear-gradient(90deg,#c9a48e,#f2b9b5)"></div>
  <h3 class="topic-title">SHARE</h3>
  <p class="topic-text">Lorem ipsum dolor sit amet, con-sectetur adipiscing elit. Fusce a laoreet massa, in euismod ligula. Curabitur a vulputate purus.</p>
</article>

<svg class="abs welcome-band" width="688" height="239" viewBox="0 0 688 239">
  <polygon points="0,16 386,16 395,0 688,0 688,223 395,223 386,239 0,239" fill="var(--grey-light)"/>
</svg>
<h2 class="abs welcome-title">Welcome to Dame Clover Haven (DCH)!</h2>
<p class="abs welcome-text" style="top:535px">My mission is simple- I want to challenge you to rethink the way you think about growing, spending and saving money. By redesigning your life around your finances I want you to run your life as if you are the CEO of your own business, and the business is maximising the value and profitability of your life.</p>
<p class="abs welcome-text" style="top:587px">It is shocking that in today's world of information we are we still live in a society where most educated people leave school without even a basic understanding of money and how to run their lives outside of a just obtaining a job. Instead, we are taught to work hard in school</p>
<span class="btn-square" style="left:135px;top:633px;width:61px;height:18px;line-height:18px">READ MORE</span>
<div class="abs" role="img" aria-label="Broken purple piggy bank with coins spilled on a wooden table" style="left:350px;top:511px;width:204px;height:138px;background:radial-gradient(circle at 55% 55%,#8d7a55,#3e3530 60%,#2a2420)"></div>

<h2 class="abs section-title">LATEST NEWS</h2>

<article class="news-card" style="left:135px">
  <div class="news-photo" role="img" aria-label="Many cupped hands holding coins" style="background:linear-gradient(135deg,#7c8a93,#b8b2ae)"><span class="news-date">Jun 10, 2019</span></div>
  <h3 class="news-title">Morbi vel nisl purus. In varius dignissim ligula quis accumsan quam</h3>
  <p class="news-text">Lorem ipsum dolor sit amet, consectetur adipiscing elit. Donec ut finibus enim. Donec sollicitudin turpis justo, sit amet porttitor lorem dictum sit amet.</p>
</article>
<article class="news-card" style="left:279px">
  <div class="news-photo" role="img" aria-label="Hand placing coins beside stacks on a chart" style="background:linear-gradient(135deg,#3f5f8c,#c9b79e)"><span class="news-date">Jun 10, 2019</span></div>
  <h3 class="news-title">Morbi vel nisl purus. In varius dignissim ligula quis accumsan quam</h3>
  <p class="news-text">Lorem ipsum dolor sit amet, consectetur adipiscing elit. Donec ut finibus enim. Donec sollicitudin turpis justo, sit amet porttitor lorem dictum sit amet.</p>
</article>
<article class="news-card" style="left:422px">
  <div class="news-photo" role="img" aria-label="Happy woman with a phone and banknotes flying around" style="background:linear-gradient(135deg,#6e6e6a,#a7a39b)"><span class="news-date">Jun 10, 2019</span></div>
  <h3 class="news-title">Morbi vel nisl purus. In varius dignissim ligula quis accumsan quam</h3>
  <p class="news-text">Lorem ipsum dolor sit amet, consectetur adipiscing elit. Donec ut finibus enim. Donec sollicitudin turpis justo, sit amet porttitor lorem dictum sit amet.</p>
</article>
<span class="btn-square" style="left:300px;top:922px;width:87px;height:22px;line-height:22px">VIEW MORE NEWS</span>

<section class="abs newsletter">
  <h2>SUBSCRIBE TO OUR NEWSLETTER</h2>
  <p>Subscribe to our newsletter to get latest news</p>
  <div class="email-field">Your email address
    <svg style="position:absolute;right:7px;top:5px" width="7" height="6" viewBox="0 0 7 6"><path d="M0.5 3 L6.5 0.5 L5 5.5 L3.3 3.6 Z" fill="none" stroke="var(--pink)" stroke-width=".6"/></svg>
  </div>
</section>

<footer class="abs site-footer">
  <div class="footer-brand">Dame Clover Haven</div>
  <span class="footer-divider"></span>
  <span class="contact-icon" style="left:247px">
    <svg width="8" height="8" viewBox="0 0 8 8"><path d="M4 7.8 C2 5.3 1.3 4 1.3 2.9 A2.7 2.7 0 0 1 6.7 2.9 C6.7 4 6 5.3 4 7.8Z" fill="var(--pink-soft)"/><circle cx="4" cy="2.9" r="1" fill="#fff"/></svg>
  </span>
  <p class="contact-text" style="left:274px">123, Building Name,<br>Street Name, Area Name,<br>Country, Zip code.</p>
  <span class="contact-icon" style="left:363px">
    <svg width="8" height="8" viewBox="0 0 8 8"><path d="M1.2 .8 L2.8 .6 L3.5 2.5 L2.6 3.2 C3.1 4.3 3.8 5 4.9 5.5 L5.6 4.6 L7.5 5.3 L7.3 6.9 C4 7.2 .9 4.1 1.2 .8Z" fill="var(--pink-soft)"/></svg>
  </span>
  <p class="contact-text" style="left:389px">Phone<br>(000) 123 4567</p>
  <span class="contact-icon" style="left:457px">
    <svg width="8" height="8" viewBox="0 0 8 8"><rect x=".5" y="1.5" width="7" height="5" rx=".6" fill="var(--pink-soft)"/><path d="M.8 2 L4 4.4 L7.2 2" fill="none" stroke="#fff" stroke-width=".6"/></svg>
  </span>
  <p class="contact-text" style="left:484px">Email<br>info@damecloverhaven.com</p>
  <span class="footer-rule"></span>
  <p class="copyright">Copyright © 2019 damecloverhaven. All Rights Reserved</p>
  <span class="social" style="left:496px" aria-label="Social link"></span>
  <span class="social" style="left:514px" aria-label="Social link"></span>
  <span class="social" style="left:531px" aria-label="Social link"></span>
  <span class="social" style="left:548px" aria-label="Social link"></span>
</footer>

</body>
</html>
```